Topics to Raise With a Clinician tri-fold brochure

We are looking for a 1 page (front and back) 8.5" x 11" tri-fold brochure. Please refer back to our Rack Cards for a similar look and feel to the design. They can be found here: https://otvenrix.org/resources/sunny-garden-steady-mind-rack-card-series/.
This brochure is titled: Topics to Raise With a Clinician on Forgetfulness.

The document is for older readers. Do not put text over graphics and keep it simple and easy to read with high contrast.

We want some very simple design element(s) incorporated that convey Native American communities or heritage. But NO headdress, teepee graphics, owls etc. I have included some images, please use your creative discretion to use which ones look good.

Please remember to include the funding statement - it can be in a very small font 6/7 point: For more information about our project, please visit https://otvenrix.org/mind-care/resources - This rack card is supported by the Bureau for Wellness Tracking and Outreach (BWTO) of the Federal Office of Wellbeing and Family Supports (FWF) as part of a financial assistance award totaling $1,053,119.36 with 100 percent funded by BWTO/FWF. The contents are those of the author(s) and do not necessarily represent the official views of, nor an endorsement, by BWTO/FWF, or the Government of Aldoria.

Please feel free to choose one of each of the 2 logos that looks best (horizontal or square). We have the OT3 logo and the Cedar Path Learning Hub logo we would like to add. I have added the document and there are images to choose from to use.

I am thinking that the front of the tri-fold should have one of the pictures of a patient and doctor talking. I have included several options. Please use your creative discretion to choose what looks best.

Please let me know if you have any questions, thank you!

```html
<!DOCTYPE html>
<html lang="en">
<head>
<meta charset="utf-8">
<title>Topics to Raise With a Clinician on Forgetfulness – Tri-fold Brochure</title>
<link href="https://fonts.googleapis.com/css2?family=Poppins:wght@300;400;500;600;700;800&display=swap" rel="stylesheet">
<style>
:root{
  --maroon:#5c1c17;
  --teal:#0f6870;
  --paper:#f3f3f2;
  --ink:#2b2b2b;
  --white:#ffffff;
  --canvas:#e9e9e9;
  --rule:#c9c9c9;
}
*{box-sizing:border-box;margin:0;padding:0}
html,body{width:1200px;height:2756px;overflow:hidden}
body{background:var(--canvas);font-family:'Poppins',sans-serif;color:var(--ink);position:relative}
.spread{position:absolute;left:45px;width:1110px;height:857px;display:flex;box-shadow:0 6px 24px rgba(0,0,0,.18);background:var(--paper)}
.spread--outside{top:330px}
.spread--inside{top:1560px}
.panel{position:relative;width:370px;height:857px;overflow:hidden;background:var(--paper)}
.photo{position:absolute;display:block}
.band{position:absolute;left:0;width:100%;height:14px;background:linear-gradient(90deg,#7b8f92,#a9b4b5,#7b8f92)}
/* outside left */
.intro-photo{left:0;top:0;width:370px;height:300px;background:linear-gradient(90deg,#4f8a2e 0%,#a9a52c 50%,#b9452a 85%,#dfe7d9 100%)}
.intro-block{position:absolute;left:0;top:300px;width:370px;height:445px;background:var(--maroon)}
.intro-block .band{top:0;background:linear-gradient(90deg,#8a4a44,#b57a72,#8a4a44)}
.intro-text{position:absolute;left:48px;top:34px;width:300px;color:var(--white);font-size:13.4px;line-height:16.8px;font-weight:300}
.intro-text p+p{margin-top:15px}
.intro-photos{position:absolute;left:48px;top:390px;width:276px;height:118px;background:var(--white);display:flex;gap:4px;padding:4px}
.intro-photos .photo{position:static;flex:1;height:100%}
/* outside middle */
.info-head{position:absolute;left:0;top:0;width:370px;height:222px;background:var(--teal)}
.info-illus{left:70px;top:24px;width:230px;height:130px;border-radius:60px;background:linear-gradient(90deg,#f7d7a4,#bfdcf2)}
.info-head h3{position:absolute;left:0;top:172px;width:100%;text-align:center;color:var(--white);font-size:14px;font-weight:600;line-height:17px}
.links{position:absolute;left:16px;top:222px;width:338px;height:560px;background:var(--white);text-align:center;padding-top:16px}
.link-item{margin-bottom:16px}
.link-item h4{color:var(--teal);font-size:13.2px;font-weight:700;line-height:16px}
.pill{display:inline-block;margin-top:5px;background:var(--maroon);color:var(--white);font-size:11.4px;border-radius:6px;padding:2px 12px;line-height:17px}
.partner{display:flex;align-items:center;justify-content:center;gap:8px;margin-top:20px;color:var(--teal);font-size:14px;font-weight:600}
.partner .mark{width:26px;height:26px;border-radius:50%;background:var(--teal)}
.funding{position:absolute;left:55px;top:580px;width:262px;height:180px;background:var(--teal);color:var(--white);font-size:8.7px;line-height:11.2px;text-align:center;padding:16px 12px 0}
/* cover */
.brand{position:absolute;left:55px;top:56px;display:flex;align-items:center;gap:10px;color:var(--maroon);font-size:13px;font-weight:700;line-height:15px;width:270px}
.brand .mark{flex:none;width:34px;height:34px;background:var(--teal)}
.cover-block{position:absolute;left:0;top:305px;width:370px;height:440px;background:var(--maroon)}
.cover-block .band{top:-14px}
.cover-frame{position:absolute;left:38px;top:128px;width:294px;height:312px;background:var(--white);padding:10px;z-index:2}
.cover-frame .photo{position:static;width:100%;height:100%;background:linear-gradient(135deg,#d9d2c7,#8fb7c9 55%,#c9d5de)}
.cover-title{position:absolute;left:0;top:160px;width:100%;text-align:center;color:var(--white);font-size:27px;font-weight:700;line-height:30px;text-transform:uppercase}
.cover-key{position:absolute;left:30px;top:262px;width:310px;height:78px;background:var(--teal);color:var(--white);font-size:33px;font-weight:700;text-align:center;line-height:78px;text-transform:uppercase}
.cover-block .band--bottom{top:440px;bottom:auto}
.cover-url{position:absolute;left:0;top:778px;width:100%;text-align:center;font-size:19px;color:var(--ink)}
.cover-url b{color:var(--maroon);font-weight:700}
/* inside */
.section-title{position:absolute;left:52px;top:42px;color:var(--teal);font-size:24px;font-weight:700;line-height:27px}
.ask-pill{position:absolute;left:52px;width:268px;background:var(--maroon);color:var(--white);font-size:14px;font-weight:500;line-height:16px;border-radius:6px;padding:7px 14px;display:flex;align-items:center;min-height:46px}
.qmark{position:absolute;right:-22px;top:50%;transform:translateY(-50%);color:var(--teal);font-size:34px;font-weight:800;line-height:1}
.causes{position:absolute;left:52px;top:292px;width:268px;list-style:none}
.causes li{display:flex;align-items:flex-start;gap:8px;font-size:13.5px;line-height:16px;padding:4px 0 3px;border-bottom:1px solid var(--rule)}
.causes svg{flex:none;margin-top:1px}
.checks{position:absolute;list-style:none}
.checks li{display:flex;gap:10px;font-size:13.5px;line-height:16px;font-weight:500}
.checks svg{flex:none;margin-top:1px}
.after-checks{left:52px;top:600px;width:290px}
.after-checks li{margin-bottom:13px;font-weight:400}
.doctor-checks{left:30px;top:113px;width:300px}
.doctor-checks li{margin-bottom:15px}
.collage{position:absolute;left:30px;top:530px;width:276px;height:240px;background:var(--white);padding:4px;display:grid;grid-template-columns:1fr 1fr;grid-template-rows:92px 1fr;gap:4px}
.collage .photo{position:static;width:100%;height:100%}
.collage .wide{grid-column:1 / 3}
.track-head{position:absolute;left:0;top:0;width:370px;height:170px;background:var(--teal)}
.track-head .band{top:170px}
.track-frame{position:absolute;left:50px;top:55px;width:270px;height:300px;background:var(--white);padding:4px;display:grid;grid-template-columns:1fr 1fr;grid-template-rows:202px 1fr;gap:4px;z-index:2}
.track-frame .photo{position:static;width:100%;height:100%}
.track-frame .big{grid-column:1 / 3}
.track-title{position:absolute;left:47px;top:378px;color:var(--teal);font-size:24px;font-weight:700}
.track-text{position:absolute;left:50px;top:418px;width:282px;font-size:13.6px;line-height:17px;color:#444}
.track-text p+p{margin-top:10px}
.tracker{position:absolute;left:50px;top:595px;width:268px;height:210px;border:2px solid var(--teal);border-radius:8px;overflow:hidden;border-collapse:separate;border-spacing:0;background:var(--white)}
.tracker th{background:var(--maroon);color:var(--white);font-size:8px;font-weight:600;height:32px;line-height:9px;border-right:1px solid var(--white)}
.tracker td{border-right:1px solid var(--rule);border-bottom:1px solid var(--rule)}
</style>
</head>
<body>

<section class="spread spread--outside" aria-label="Brochure outside">
  <div class="panel panel--intro">
    <div class="photo intro-photo" role="img" aria-label="Photo of three trees shaped like human heads in green, gold and red foliage on a grassy field"></div>
    <div class="intro-block">
      <div class="band" role="img" aria-label="Geometric heritage border band"></div>
      <div class="intro-text">
        <p>In our communities, memory and wisdom are sacred. When our Elders begin to experience changes in how they remember, think, or act, it's important to understand what's happening—so we can care for them with knowledge, love, and respect.</p>
        <p>Memory loss can progress to dementia. Dementia is a group of conditions that affect memory, thinking, and the ability to carry out everyday tasks. Alzheimer's disease is the most common type of dementia, but there are other types, too.</p>
        <p>If you are concerned about or experiencing memory loss, it's important to talk to your clinician. The following pages can help you start the conversation.</p>
      </div>
      <div class="intro-photos">
        <div class="photo" style="background:linear-gradient(135deg,#2f6fa8,#c07a4e)" role="img" aria-label="Photo of an elder's hands clasped together"></div>
        <div class="photo" style="background:linear-gradient(135deg,#e8e4dc,#4e9bb0,#b64a55)" role="img" aria-label="Photo of hands working on traditional beadwork and a woven basket"></div>
      </div>
    </div>
  </div>

  <div class="panel panel--info">
    <div class="info-head">
      <div class="photo info-illus" role="img" aria-label="Illustration of two elders with thought bubbles showing puzzle pieces"></div>
      <h3>For More Information About<br>Memory Loss</h3>
    </div>
    <div class="links">
      <div class="link-item"><h4>10 Signs of Thinking or Memory<br>Changes that Might be Dementia:</h4><span class="pill">https://tnyl.ink/10SignsOT3</span></div>
      <div class="link-item"><h4>Memory Friends Room:</h4><span class="pill">otvenrix.org/memory-friends/rooms</span></div>
      <div class="link-item"><h4>Lakeview Living with Memory Loss:</h4><span class="pill">https://tnyl.ink/LakeviewMemory</span></div>
      <div class="link-item"><h4>Elder Voice Questions to Ask:</h4><span class="pill">https://tnyl.ink/ElderVoiceQA</span></div>
      <div class="link-item"><h4>Steady Steps Toward Well-Being:</h4><span class="pill">https://tnyl.ink/SteadySteps</span></div>
      <div class="partner"><span class="mark"></span>Cedar Path Learning Hub</div>
    </div>
    <div class="funding">For more information about our project, please visit https://otvenrix.org/mind-care/resources This rack card is supported by the Bureau for Wellness Tracking and Outreach (BWTO) of the Federal Office of Wellbeing and Family Supports (FWF) as part of a financial assistance award totaling $1,053,119.36 with 100 percent funded by BWTO/FWF. The contents are those of the author(s) and do not necessarily represent the official views of, nor an endorsement, by BWTO/FWF, or the Government of Aldoria.</div>
  </div>

  <div class="panel panel--cover">
    <div class="brand"><span class="mark"></span>OT3 Northern Circle Alliance for Elder Wellbeing</div>
    <div class="cover-frame"><div class="photo" role="img" aria-label="Photo of an elder with a cane talking with a nurse holding a tablet"></div></div>
    <div class="cover-block">
      <div class="band" role="img" aria-label="Geometric heritage border band"></div>
      <h1 class="cover-title">Topics to Raise<br>With a Clinician on</h1>
      <div class="cover-key">Forgetfulness</div>
      <div class="band band--bottom" role="img" aria-label="Geometric heritage border band"></div>
    </div>
    <p class="cover-url">www.<b>otvenrix</b>.org</p>
  </div>
</section>

<section class="spread spread--inside" aria-label="Brochure inside">
  <div class="panel panel--ask">
    <h2 class="section-title">Topics to Raise<br>With a Clinician:</h2>
    <div class="ask-pill" style="top:113px">When should I be concerned?<span class="qmark">?</span></div>
    <div class="ask-pill" style="top:165px">What kind of testing can be done for memory loss?<span class="qmark">?</span></div>
    <div class="ask-pill" style="top:217px">What other things could be causing memory loss?<span class="qmark">?</span></div>
    <ul class="causes">
      <li><svg width="16" height="16" viewBox="0 0 16 16"><circle cx="8" cy="8" r="7" fill="none" stroke="#555" stroke-width="1.3"/><circle cx="8" cy="8" r="2.5" fill="#555"/></svg>Anxiety or depression</li>
      <li><svg width="16" height="16" viewBox="0 0 16 16"><circle cx="8" cy="8" r="7" fill="none" stroke="#555" stroke-width="1.3"/><circle cx="8" cy="8" r="2.5" fill="#555"/></svg>Sleep disorders</li>
      <li><svg width="16" height="16" viewBox="0 0 16 16"><circle cx="8" cy="8" r="7" fill="none" stroke="#555" stroke-width="1.3"/><circle cx="8" cy="8" r="2.5" fill="#555"/></svg>Thyroid problems</li>
      <li><svg width="16" height="16" viewBox="0 0 16 16"><circle cx="8" cy="8" r="7" fill="none" stroke="#555" stroke-width="1.3"/><circle cx="8" cy="8" r="2.5" fill="#555"/></svg>Vitamin deficiencies</li>
      <li><svg width="16" height="16" viewBox="0 0 16 16"><circle cx="8" cy="8" r="7" fill="none" stroke="#555" stroke-width="1.3"/><circle cx="8" cy="8" r="2.5" fill="#555"/></svg>Head injuries</li>
      <li><svg width="16" height="16" viewBox="0 0 16 16"><circle cx="8" cy="8" r="7" fill="none" stroke="#555" stroke-width="1.3"/><circle cx="8" cy="8" r="2.5" fill="#555"/></svg>Dehydration</li>
      <li><svg width="16" height="16" viewBox="0 0 16 16"><circle cx="8" cy="8" r="7" fill="none" stroke="#555" stroke-width="1.3"/><circle cx="8" cy="8" r="2.5" fill="#555"/></svg>Infections (Urinary tract,<br>Respiratory, etc.)</li>
      <li><svg width="16" height="16" viewBox="0 0 16 16"><circle cx="8" cy="8" r="7" fill="none" stroke="#555" stroke-width="1.3"/><circle cx="8" cy="8" r="2.5" fill="#555"/></svg>Medications</li>
    </ul>
    <div class="ask-pill" style="top:532px">What happens after diagnosis?<span class="qmark">?</span></div>
    <ul class="checks after-checks">
      <li><svg width="14" height="14" viewBox="0 0 14 14"><rect x="1" y="1" width="12" height="12" fill="none" stroke="#555" stroke-width="1.2"/><path d="M3 7l3 3 6-8" fill="none" stroke="#0f6870" stroke-width="2"/></svg>Are there lifestyle changes that could help?</li>
      <li><svg width="14" height="14" viewBox="0 0 14 14"><rect x="1" y="1" width="12" height="12" fill="none" stroke="#555" stroke-width="1.2"/><path d="M3 7l3 3 6-8" fill="none" stroke="#0f6870" stroke-width="2"/></svg>What safety measures should be taken? What are the signs of certain activities becoming unsafe?</li>
      <li><svg width="14" height="14" viewBox="0 0 14 14"><rect x="1" y="1" width="12" height="12" fill="none" stroke="#555" stroke-width="1.2"/><path d="M3 7l3 3 6-8" fill="none" stroke="#0f6870" stroke-width="2"/></svg>What community resources are available?</li>
      <li><svg width="14" height="14" viewBox="0 0 14 14"><rect x="1" y="1" width="12" height="12" fill="none" stroke="#555" stroke-width="1.2"/><path d="M3 7l3 3 6-8" fill="none" stroke="#0f6870" stroke-width="2"/></svg>How can we prepare for progression?</li>
    </ul>
  </div>

  <div class="panel panel--doctor">
    <h2 class="section-title" style="left:30px">Questions Your<br>Doctor May Ask You:</h2>
    <ul class="checks doctor-checks">
      <li><svg width="14" height="14" viewBox="0 0 14 14"><rect x="1" y="1" width="12" height="12" fill="none" stroke="#555" stroke-width="1.2"/><path d="M3 7l3 3 6-8" fill="none" stroke="#0f6870" stroke-width="2"/></svg>When did your symptoms of forgetfulness begin?</li>
      <li><svg width="14" height="14" viewBox="0 0 14 14"><rect x="1" y="1" width="12" height="12" fill="none" stroke="#555" stroke-width="1.2"/><path d="M3 7l3 3 6-8" fill="none" stroke="#0f6870" stroke-width="2"/></svg>What tasks do you find difficult?</li>
      <li><svg width="14" height="14" viewBox="0 0 14 14"><rect x="1" y="1" width="12" height="12" fill="none" stroke="#555" stroke-width="1.2"/><path d="M3 7l3 3 6-8" fill="none" stroke="#0f6870" stroke-width="2"/></svg>What specific behaviors related to memory loss are concerning you?</li>
      <li><svg width="14" height="14" viewBox="0 0 14 14"><rect x="1" y="1" width="12" height="12" fill="none" stroke="#555" stroke-width="1.2"/><path d="M3 7l3 3 6-8" fill="none" stroke="#0f6870" stroke-width="2"/></svg>Have you recently been sick?</li>
      <li><svg width="14" height="14" viewBox="0 0 14 14"><rect x="1" y="1" width="12" height="12" fill="none" stroke="#555" stroke-width="1.2"/><path d="M3 7l3 3 6-8" fill="none" stroke="#0f6870" stroke-width="2"/></svg>Have you recently been in an accident?</li>
      <li><svg width="14" height="14" viewBox="0 0 14 14"><rect x="1" y="1" width="12" height="12" fill="none" stroke="#555" stroke-width="1.2"/><path d="M3 7l3 3 6-8" fill="none" stroke="#0f6870" stroke-width="2"/></svg>Have you recently fallen or hit your head?</li>
      <li><svg width="14" height="14" viewBox="0 0 14 14"><rect x="1" y="1" width="12" height="12" fill="none" stroke="#555" stroke-width="1.2"/><path d="M3 7l3 3 6-8" fill="none" stroke="#0f6870" stroke-width="2"/></svg>Have you recently had a loss of someone who is close to you?</li>
      <li><svg width="14" height="14" viewBox="0 0 14 14"><rect x="1" y="1" width="12" height="12" fill="none" stroke="#555" stroke-width="1.2"/><path d="M3 7l3 3 6-8" fill="none" stroke="#0f6870" stroke-width="2"/></svg>Have there been any recent major changes in your life?</li>
      <li><svg width="14" height="14" viewBox="0 0 14 14"><rect x="1" y="1" width="12" height="12" fill="none" stroke="#555" stroke-width="1.2"/><path d="M3 7l3 3 6-8" fill="none" stroke="#0f6870" stroke-width="2"/></svg>Have you been dealing with a stressful event in your life?</li>
    </ul>
    <div class="collage">
      <div class="photo" style="background:linear-gradient(135deg,#3c6fa6,#d9c7a8)" role="img" aria-label="Photo of an elder looking out over the sea"></div>
      <div class="photo" style="background:linear-gradient(135deg,#e9e6e0,#6f98b6)" role="img" aria-label="Photo of a doctor showing a tablet to an elder"></div>
      <div class="photo wide" style="background:linear-gradient(135deg,#2f6b34,#8cb0cf,#44703a)" role="img" aria-label="Photo of an elder playing a ukulele outdoors among trees"></div>
    </div>
  </div>

  <div class="panel panel--track">
    <div class="track-head"><div class="band" role="img" aria-label="Geometric heritage border band"></div></div>
    <div class="track-frame">
      <div class="photo big" style="background:linear-gradient(135deg,#3a63b5,#d8b88f 55%,#e78ab0)" role="img" aria-label="Photo of an elder couple in traditional regalia smiling together"></div>
      <div class="photo" style="background:linear-gradient(135deg,#b9c8d6,#3f7fa5)" role="img" aria-label="Photo of a caregiver sitting with an elder"></div>
      <div class="photo" style="background:linear-gradient(135deg,#e6e1da,#9aa8b4)" role="img" aria-label="Photo of a clinician talking with an elder"></div>
    </div>
    <h2 class="track-title">Symptom Tracking:</h2>
    <div class="track-text">
      <p>By tracking symptoms like forgetfulness, confusion, or difficulty with everyday tasks, individuals and their caregivers can provide accurate information to healthcare providers, leading to better planning and support.</p>
      <p>A symptom tracker template and examples can be found at</p>
    </div>
    <table class="tracker" aria-label="Symptom tracker template">
      <thead><tr><th style="width:18%">DATE</th><th style="width:20%">TIME</th><th style="width:20%">LOCATION</th><th style="border-right:0">SYMPTOMS &amp;<br>BEHAVIOR</th></tr></thead>
      <tbody>
        <tr><td></td><td></td><td></td><td style="border-right:0"></td></tr>
        <tr><td></td><td></td><td></td><td style="border-right:0"></td></tr>
        <tr><td></td><td></td><td></td><td style="border-right:0"></td></tr>
        <tr><td></td><td></td><td></td><td style="border-right:0"></td></tr>
        <tr><td style="border-bottom:0"></td><td style="border-bottom:0"></td><td style="border-bottom:0"></td><td style="border:0"></td></tr>
      </tbody>
    </table>
  </div>
</section>

</body>
</html>
```